WEB PAGES DESIGN

We need a web design for a new company called "NEXO47". Our major business is that provide Internet Data Center solution, such as: rack/colocation, bandwidth, dedicated server, cloud server, CDN, and so on.
Requirements of Design:
1. Home page layout can refer to index-content.jpg in the attachments, but not limited.
2. According to match logo colors to design colors of web pages, Logo in the attachments.
3. The web contents of home page in image of the index-content.jpg.
4. The successful bidder will need to design three banner.

```html
<!DOCTYPE html>
<html lang="en">
<head>
<meta charset="utf-8">
<title>NEXO47 — IDC Solutions</title>
<link href="https://fonts.googleapis.com/css2?family=Questrial&family=Alfa+Slab+One&display=swap" rel="stylesheet">
<style>
:root{
  --ink:#222;
  --text:#3a3a3a;
  --muted:#555;
  --dark:#3d3d3d;
  --green:#8cc63f;
  --green-deep:#3f7a2a;
  --green-soft:#c8f5b4;
  --page:#ebf5ea;
  --header:#f5fafb;
  --white:#fff;
}
*{margin:0;padding:0;box-sizing:border-box}
html,body{width:737px;height:1200px;overflow:hidden}
body{position:relative;background:var(--page);font-family:"Questrial",Arial,sans-serif;color:var(--text)}
.abs{position:absolute}
.topbar{left:0;top:0;width:737px;height:12px;background:var(--dark)}
.header{left:0;top:12px;width:737px;height:69px;background:var(--header);border-bottom:1px solid #ccc}
.brand{left:128px;top:28px;display:flex;align-items:center;gap:6px;font-size:16px;color:var(--ink);letter-spacing:1px}
.brand-mark{width:14px;height:14px;background:var(--green)}
.nav{left:294px;top:52px;display:flex;font-size:9px;color:var(--ink)}
.nav a{color:inherit;text-decoration:none;padding:0 8px;line-height:17px}
.nav .active{background:var(--dark);color:var(--white);width:52px;text-align:center;border-radius:3px 3px 0 0;margin-right:6px}
.banner{left:0;top:81px;width:737px;height:299px;background:linear-gradient(90deg,#2d3a34 0%,#4a6b4e 25%,#5ea548 55%,#4e9a3a 80%,#2f6a25 100%)}
.banner-person{left:120px;top:140px;width:152px;height:240px;background:linear-gradient(180deg,#3a3e44,#1e2226)}
.banner-title{left:295px;top:165px;width:308px;height:53px;background:var(--green-soft);font-family:"Alfa Slab One",Georgia,serif;font-size:25px;color:#2b2b2b;padding:10px 0 0 11px;letter-spacing:.5px}
.banner-copy{left:295px;top:221px;width:320px;font-size:15px;line-height:16.5px;color:var(--white)}
.banner-btn{left:296px;top:282px;width:89px;height:21px;background:linear-gradient(#f4f4f4,#c9c9c9);font-size:10px;color:#333;text-align:center;line-height:21px}
.dots{left:364px;top:340px;display:flex;gap:3px}
.dots i{width:5px;height:5px;border-radius:50%;background:#333;display:block}
.arrow-box{width:18px;height:18px;background:var(--green-deep)}
.section-title{left:127px;top:393px;font-size:18px;color:var(--ink)}
.product-img{width:237px;height:100px;background:linear-gradient(90deg,#8ea0ad,#4a5766 55%,#1d232b)}
.product-img.selected{border:4px solid var(--green)}
.product-name{font-size:13.5px;color:var(--ink)}
.product-copy{width:215px;font-size:8.5px;line-height:12px;color:var(--muted)}
.btn{width:59px;height:18px;background:var(--dark);color:var(--white);font-size:7px;text-align:center;line-height:18px;border-radius:2px}
.btn.active{background:var(--green)}
.partners{left:0;top:872px;width:737px;height:125px;background:var(--green)}
.partner{top:886px;width:149px;height:99px;background:linear-gradient(180deg,#e6eef3,#b9c6cf)}
.partner-name{top:30px;width:100%;text-align:center;font-size:15px;color:#555}
.partner-cap{left:0;bottom:0;width:100%;height:37px;background:rgba(80,80,80,.85);color:var(--white);font-size:6px;line-height:8px;padding:9px 8px 0 10px}
.foot-title{font-size:13px;color:var(--ink)}
.news{left:131px;top:1055px;list-style:none;font-size:7.5px;line-height:14.2px;color:var(--muted)}
.news li::before{content:"";display:inline-block;border-left:4px solid #333;border-top:3px solid transparent;border-bottom:3px solid transparent;margin-right:8px}
.foot-brand{left:343px;top:1068px;display:flex;align-items:center;gap:5px;font-size:14px;color:var(--ink);letter-spacing:1px}
.contact{left:449px;top:1053px;font-size:7.5px;line-height:13px;color:var(--ink)}
.contact strong{font-weight:400;font-size:10.5px}
.contact .phone{font-size:10.5px}
.social{left:452px;top:1120px;display:flex;gap:12px}
.social i{display:block;width:26px;height:26px;border-radius:50%;background:#333}
.chat-dot{left:565px;top:1058px;width:36px;height:36px;border-radius:50%;background:#7bc24a}
.bottombar{left:0;top:1172px;width:737px;height:28px;background:#3a3a3a;color:var(--white);font-size:6.5px;line-height:28px}
</style>
</head>
<body>
<div class="abs topbar"></div>
<header class="abs header"></header>
<div class="abs brand"><span class="brand-mark"></span>NEXO47</div>
<nav class="abs nav"><a class="active">Home</a><a>Dedicated server</a><a>Hosting</a><a>Data Center</a><a>About Us</a></nav>

<section class="abs banner" role="img" aria-label="Server room with green-lit data center racks"></section>
<div class="abs banner-person" role="img" aria-label="Smiling businessman in a suit with arms crossed"></div>
<div class="abs banner-title">IDC SOLUTIONS</div>
<p class="abs banner-copy">NEXO47 provides a wide range of highly specialized solutions that utilizes technology to transform your organization</p>
<div class="abs banner-btn">Read more</div>
<div class="abs dots"><i></i><i></i><i></i></div>
<svg class="abs" style="left:41px;top:201px" width="18" height="18"><rect width="18" height="18" fill="#3f7a2a"/><path d="M11 5 L7 9 L11 13" stroke="#fff" stroke-width="2" fill="none"/></svg>
<svg class="abs" style="left:652px;top:201px" width="18" height="18"><rect width="18" height="18" fill="#2f5a22"/><path d="M7 5 L11 9 L7 13" stroke="#fff" stroke-width="2" fill="none"/></svg>

<h2 class="abs section-title" style="font-weight:400">Our Products</h2>

<div class="abs product-img selected" style="left:119px;top:425px" role="img" aria-label="Business handshake"></div>
<div class="abs product-img" style="left:369px;top:425px" role="img" aria-label="Business handshake"></div>
<div class="abs product-img" style="left:119px;top:641px" role="img" aria-label="Business handshake"></div>
<div class="abs product-img" style="left:369px;top:641px" role="img" aria-label="Business handshake"></div>

<h3 class="abs product-name" style="left:126px;top:532px;font-weight:400">Dedicated Servers</h3>
<p class="abs product-copy" style="left:126px;top:553px">Lorem gubergren amet at consetetur ut illum ea dignissim dolores. Sed at commodo vero in dolore dolor kasd gubergren. Diam labore molestie</p>
<div class="abs btn active" style="left:127px;top:604px">read more »</div>

<h3 class="abs product-name" style="left:377px;top:532px;font-weight:400">Servers Hosting</h3>
<p class="abs product-copy" style="left:377px;top:553px">Lorem gubergren amet at consetetur ut illum ea dignissim dolores. Sed at commodo vero in dolore dolor kasd gubergren. Diam labore molestie</p>
<div class="abs btn" style="left:377px;top:604px">read more »</div>

<h3 class="abs product-name" style="left:128px;top:749px;font-weight:400">Rack &amp; Bandwidth</h3>
<p class="abs product-copy" style="left:128px;top:770px">Lorem gubergren amet at consetetur ut illum ea dignissim dolores. Sed at commodo vero in dolore dolor kasd gubergren. Diam labore molestie</p>
<div class="abs btn" style="left:128px;top:821px">read more »</div>

<h3 class="abs product-name" style="left:377px;top:749px;font-weight:400">Reseller &amp; Referral</h3>
<p class="abs product-copy" style="left:377px;top:770px">Lorem gubergren amet at consetetur ut illum ea dignissim dolores. Sed at commodo vero in dolore dolor kasd gubergren. Diam labore molestie</p>
<div class="abs btn" style="left:377px;top:821px">read more »</div>

<section class="abs partners"></section>
<svg class="abs" style="left:72px;top:917px" width="24" height="42"><path d="M20 3 L5 21 L20 39" stroke="#3d3d3d" stroke-width="6" fill="none"/></svg>
<svg class="abs" style="left:619px;top:917px" width="24" height="42"><path d="M4 3 L19 21 L4 39" stroke="#3d3d3d" stroke-width="6" fill="none"/></svg>
<div class="abs partner" style="left:123px" role="img" aria-label="Team of office workers"><div class="abs partner-name">Partner # 1</div><div class="abs partner-cap">vero in dolore dolor kasd gubergren. Diam labore molestie sadipscing read more »</div></div>
<div class="abs partner" style="left:287px" role="img" aria-label="Team of office workers"><div class="abs partner-name">Partner # 2</div><div class="abs partner-cap">vero in dolore dolor kasd gubergren. Diam labore molestie sadipscing read more »</div></div>
<div class="abs partner" style="left:451px" role="img" aria-label="Team of office workers"><div class="abs partner-name">Partner # 3</div><div class="abs partner-cap">vero in dolore dolor kasd gubergren. Diam labore molestie sadipscing read more »</div></div>

<h4 class="abs foot-title" style="left:128px;top:1032px;font-weight:400">Latest New</h4>
<ul class="abs news">
<li>Lorem gubergren amet at consetetur ut</li>
<li>illum ea dignissim dolores. Sed at</li>
<li>commodo vero in dolore dolor kasd</li>
<li>gubergren. Diam labore molestie</li>
<li>sadipscing labore ipsum dolores.</li>
<li>Takimata ea consectetuer magna.</li>
</ul>
<div class="abs foot-brand"><span class="brand-mark"></span>NEXO47</div>

<h4 class="abs foot-title" style="left:448px;top:1029px;font-weight:400">Contact Us</h4>
<address class="abs contact" style="font-style:normal"><strong>NEXO47</strong><br>4180 Cedar Ridge Rd<br>Lakeway, TX 78734<br><span class="phone">Phone: 512-555-0147</span></address>
<div class="abs chat-dot"></div>
<div class="abs social"><i></i><i></i><i></i><i></i></div>

<footer class="abs bottombar"><span class="abs" style="left:146px">Copyright © 1999 - 2015 NEXO47 . All Rights Reserved.</span><span class="abs" style="left:422px">Terms of Service | Privacy Policy | Contact Us</span></footer>
</body>
</html>
```